Tallowreed Advisory Partners Business Card Design

We have the logo we just need someone to design a modern business card design.

Name: Desmond Munkalt
Phone: 3055550148
Mobile: 9175550193
Web:www.tallowreedadvisory.example
email: dmunkalt@tallowreedadvisory.example
Company: Tallowreed Advisory Partners
Title: CEO

Address: 718 Quillmore Ave, Miami, Florida 33190

Target Market(s)

companies over 100 employees

Industry/Entity Type

Business

```html
<!DOCTYPE html>
<html lang="en">
<head>
<meta charset="utf-8">
<title>Tallowreed Advisory Partners – Business Card</title>
<link rel="stylesheet" href="https://fonts.googleapis.com/css2?family=Exo+2:wght@300;400;600;700&family=Montserrat:wght@500;700&display=swap">
<style>
  :root {
    --backdrop: #cbcbcb;
    --card-dark: #000000;
    --card-light: #ffffff;
    --brand-blue: #4a6fc9;
    --ink: #1f1f1f;
    --ink-soft: #444444;
    --white: #ffffff;
  }
  * { margin: 0; padding: 0; box-sizing: border-box; }
  html, body {
    width: 1200px; height: 960px; overflow: hidden;
    background: var(--backdrop);
  }
  .stage { position: relative; width: 1200px; height: 960px; }
  .card {
    position: absolute; left: 276px; width: 648px; height: 360px; overflow: hidden;
  }
  .card--front { top: 80px; background: var(--card-dark); }
  .card--back { top: 494px; background: var(--card-light); }

  .line-pattern {
    position: absolute; left: 0; top: 0; width: 270px; height: 360px;
    background: radial-gradient(ellipse at 30% 45%, rgba(74,111,201,0.35), rgba(74,111,201,0.08) 60%, rgba(0,0,0,0) 80%);
  }
  .brand-mark {
    position: absolute; left: 303px; top: 42px; width: 320px; text-align: center;
    color: var(--white); font-family: "Montserrat", sans-serif; font-weight: 700;
  }
  .brand-mark__dot {
    display: block; width: 112px; height: 112px; border-radius: 50%;
    background: var(--brand-blue); margin: 0 auto 24px;
  }
  .brand-mark__name { display: block; font-size: 32px; line-height: 1; letter-spacing: 1px; }
  .brand-mark__sub { display: block; font-size: 12px; margin-top: 6px; letter-spacing: 1px; font-weight: 500; }
  .website {
    position: absolute; left: 303px; top: 312px; width: 320px; text-align: center;
    color: var(--brand-blue); font-family: "Exo 2", sans-serif; font-size: 17px;
  }

  .identity {
    position: absolute; left: 92px; top: 150px; display: flex; align-items: center;
    font-family: "Exo 2", sans-serif; color: var(--ink);
  }
  .identity__name { font-size: 33px; font-weight: 300; letter-spacing: 0.5px; }
  .identity__rule { width: 2px; height: 50px; background: var(--ink); margin: 0 20px; }
  .identity__title { font-size: 33px; font-weight: 700; }
  .identity__company {
    font-size: 8px; line-height: 1.05; margin-left: 5px; color: var(--ink-soft); font-weight: 400;
  }
  .contacts {
    position: absolute; left: 36px; top: 282px; list-style: none;
    font-family: "Exo 2", sans-serif; font-size: 12px; color: var(--ink-soft); line-height: 14.5px;
  }
  .contacts li { display: flex; align-items: center; }
  .contacts svg { width: 11px; height: 11px; margin-right: 5px; flex: none; }
  .contacts b { font-weight: 600; color: var(--ink); margin-right: 3px; }
</style>
</head>
<body>
<div class="stage">
  <section class="card card--front">
    <div class="line-pattern" role="img" aria-label="Blue line pattern decoration"></div>
    <div class="brand-mark">
      <span class="brand-mark__dot"></span>
      <span class="brand-mark__name">TALLOWREED</span>
      <span class="brand-mark__sub">ADVISORY PARTNERS</span>
    </div>
    <p class="website">www.tallowreedadvisory.example</p>
  </section>

  <section class="card card--back">
    <div class="identity">
      <span class="identity__name">Desmond Munkalt</span>
      <span class="identity__rule"></span>
      <span class="identity__title">CEO</span>
      <span class="identity__company">Tallowreed<br>Advisory<br>Partners</span>
    </div>
    <ul class="contacts">
      <li><svg viewBox="0 0 11 11"><rect width="11" height="11" rx="1.5" fill="#222"/><path d="M3 3h2v1.5L4 5.2c.4.9 1 1.5 1.8 1.8l.7-1H8v2H7C4.7 8 3 6.3 3 4z" fill="#fff"/></svg><b>Phone:</b>3055550148</li>
      <li><svg viewBox="0 0 11 11"><rect width="11" height="11" rx="1.5" fill="#222"/><rect x="3.5" y="2" width="4" height="7" rx="0.8" fill="#fff"/><rect x="4.3" y="3" width="2.4" height="4" fill="#222"/></svg><b>Mobile:</b>9175550193</li>
      <li><svg viewBox="0 0 11 11"><rect width="11" height="11" rx="1.5" fill="#222"/><rect x="2" y="3" width="7" height="5" fill="#fff"/><path d="M2 3l3.5 3L9 3" stroke="#222" stroke-width="0.8" fill="none"/></svg><b>eMail:</b>dmunkalt@tallowreedadvisory.example</li>
      <li><svg viewBox="0 0 11 11"><rect width="11" height="11" rx="1.5" fill="#222"/><path d="M5.5 2a2.3 2.3 0 0 0-2.3 2.3C3.2 6 5.5 9 5.5 9s2.3-3 2.3-4.7A2.3 2.3 0 0 0 5.5 2z" fill="#fff"/></svg><b>Address:</b>718 Quillmore Ave, Miami, Florida 33190</li>
    </ul>
  </section>
</div>
</body>
</html>
```